Podcast Cover for "The Vital Ledger"

The title of my Podcast is " The Vital Ledger with Marek Tolloway '' i'm looking to have a professional cover design that depicts just that while still utilizing the name. We know what a blueprint is but, I want you to use it in a different manner.

I want a cover art that is in a sense a blueprint or road-map of the many components of health e.i Mindfulness, Exercise, Healthcare Systems/ Hospital, Nutrition/Diet. I don't want these to be words, but instead illustration of some sort. The only words should be the title of the podcast mentioned above.

The design is vital for the identification of the podcast because the components of health listed above are just subject categories for the podcast as each will have many episodes..for example within healthcare/Hospital i would; cover something like health literacy as a barrier to healthcare; a more specific topic would be health literacy and how lack of it is disproportionately affecting black people as it relates to COVID-19.

I hope this makes sense as to how important this cover is to the success and identification of this Podcast.

Target Market(s)

Health

Requirements
Must have
• Design must follow podcast cover measurements of (3000x3000)
Should not have
• please do not use the files I uploaded. they are just example of what a blueprint looks like.

```html
<!DOCTYPE html>
<html lang="en">
<head>
<meta charset="utf-8">
<title>The Vital Ledger with Marek Tolloway</title>
<link rel="stylesheet" href="https://fonts.googleapis.com/css2?family=Montserrat:wght@400;600&display=swap">
<style>
  :root {
    --blue-light: #3a9bd0;
    --blue-mid: #2381bb;
    --blue-deep: #155f92;
    --ink: #0d3550;
    --white: #ffffff;
    --placeholder: rgba(255, 255, 255, 0.22);
  }
  * { margin: 0; padding: 0; box-sizing: border-box; }
  html, body { width: 1200px; height: 1200px; overflow: hidden; }
  body { font-family: "Montserrat", sans-serif; }

  .cover {
    position: relative;
    width: 1200px;
    height: 1200px;
    overflow: hidden;
    background: radial-gradient(circle at 50% 45%, var(--blue-light) 0%, var(--blue-mid) 55%, var(--blue-deep) 100%);
  }

  .icon {
    position: absolute;
    filter: drop-shadow(0 0 1.5px var(--ink)) drop-shadow(0 0 1px var(--ink));
  }
  .icon svg { width: 100%; height: 100%; display: block; overflow: visible; }
  .icon .line { fill: none; stroke: var(--white); stroke-width: 9; stroke-linecap: round; stroke-linejoin: round; }
  .icon .solid { fill: var(--white); }

  .icon-heart  { left: 82px;  top: 62px;  width: 308px; height: 278px; }
  .icon-runner { left: 440px; top: 62px;  width: 228px; height: 336px; border-radius: 24px;
                 background: linear-gradient(160deg, var(--placeholder), rgba(255,255,255,0.1)); filter: none; }
  .icon-pills  { left: 838px; top: 82px;  width: 274px; height: 236px; }
  .icon-apple  { left: 82px;  top: 855px; width: 292px; height: 308px; }
  .icon-noburger { left: 435px; top: 870px; width: 262px; height: 270px; }
  .icon-noburger .burger-art {
    position: absolute; left: 64px; top: 88px; width: 134px; height: 94px; border-radius: 14px;
    background: linear-gradient(180deg, var(--placeholder), rgba(255,255,255,0.12));
  }
  .icon-noburger svg { position: absolute; inset: 0; }
  .icon-ball   { left: 840px; top: 855px; width: 285px; height: 285px; }

  .title {
    position: absolute;
    left: 0; right: 0;
    color: var(--white);
    font-weight: 600;
    text-align: center;
    text-transform: uppercase;
    text-shadow: 0 0 2px var(--ink), 1px 1px 0 var(--ink), -1px -1px 0 var(--ink), 2px 3px 4px rgba(0,0,0,0.35);
  }
  .title-top { top: 428px; font-size: 106px; letter-spacing: 5px; line-height: 1; }
  .title-row {
    top: 522px;
    display: flex;
    align-items: center;
    gap: 40px;
  }
  .title-bottom { font-size: 106px; letter-spacing: 5px; line-height: 1; }
  .rule-pair {
    flex: 1;
    height: 72px;
    display: flex;
    flex-direction: column;
    justify-content: space-between;
  }
  .rule-pair span {
    display: block;
    height: 12px;
    background: var(--white);
    box-shadow: 0 0 0 1.5px var(--ink);
  }
  .host-with { top: 676px; font-size: 32px; font-weight: 400; letter-spacing: 2px; line-height: 1; }
  .host-name { top: 708px; font-size: 66px; font-weight: 400; letter-spacing: 3px; line-height: 1; }
</style>
</head>
<body>
<main class="cover">

  <div class="icon icon-heart" aria-hidden="true">
    <svg viewBox="0 0 200 180">
      <path class="line" d="M100 170 L20 90 C-5 62 8 14 52 10 C76 8 92 24 100 40 C108 24 124 8 148 10 C192 14 205 62 180 90 Z"/>
      <path class="line" d="M6 88 H62 L74 62 L90 124 L108 46 L122 88 H194"/>
    </svg>
  </div>

  <div class="icon icon-runner" role="img" aria-label="Outline of a running figure"></div>

  <div class="icon icon-pills" aria-hidden="true">
    <svg viewBox="0 0 240 200">
      <g transform="rotate(-45 78 92)">
        <rect class="line" x="8" y="62" width="140" height="60" rx="30"/>
        <path class="solid" d="M78 62 H38 A30 30 0 0 0 38 122 H78 Z"/>
      </g>
      <circle class="line" cx="182" cy="138" r="48"/>
      <line class="line" x1="138" y1="138" x2="226" y2="138"/>
    </svg>
  </div>

  <h1 class="title title-top">The Vital</h1>
  <div class="title title-row">
    <div class="rule-pair" aria-hidden="true"><span></span><span></span></div>
    <span class="title-bottom">Ledger</span>
    <div class="rule-pair" aria-hidden="true"><span></span><span></span></div>
  </div>
  <p class="title host-with">With</p>
  <p class="title host-name">Marek Tolloway</p>

  <div class="icon icon-apple" aria-hidden="true">
    <svg viewBox="0 0 200 210">
      <path class="line" d="M100 52 C80 36 30 34 14 82 C0 128 28 190 62 202 C80 208 90 198 100 198 C110 198 120 208 138 202 C172 190 200 128 186 82 C170 34 120 36 100 52 Z"/>
      <path class="line" d="M100 52 C100 34 104 20 112 8"/>
      <path class="line" d="M110 30 C118 10 146 4 160 8 C154 28 132 38 110 30 Z"/>
      <path class="line" d="M150 100 C160 130 154 160 136 182"/>
    </svg>
  </div>

  <div class="icon icon-noburger">
    <div class="burger-art" role="img" aria-label="Burger icon, crossed out"></div>
    <svg viewBox="0 0 200 200" aria-hidden="true">
      <circle class="line" cx="100" cy="100" r="94"/>
      <line class="line" x1="34" y1="34" x2="166" y2="166"/>
    </svg>
  </div>

  <div class="icon icon-ball" aria-hidden="true">
    <svg viewBox="0 0 200 200">
      <circle class="line" cx="100" cy="100" r="94"/>
      <path class="line" d="M14 62 C70 80 130 80 186 62"/>
      <path class="line" d="M14 138 C70 120 130 120 186 138"/>
    </svg>
  </div>

</main>
</body>
</html>
```